Breezeway Comfort business cards design

Need a business card design for a Heating and Air Conditioning business. I need these items included.
Business name: Breezeway Comfort
Owner: Marcus Tollefsen
License # 2874590
Phone number # 555-382-4071
Email: breezewaycomfortair@mailvista.example
Sales
Service
Installation
Maintenance

Heating and Air Conditioning

Requirements
Must have
• Company name , license number , phone number , email

```html
<!DOCTYPE html>
<html lang="en">
<head>
<meta charset="utf-8">
<title>Breezeway Comfort – Business Cards</title>
<link rel="stylesheet" href="https://fonts.googleapis.com/css2?family=Montserrat:wght@400;500;600;700;800&display=swap">
<style>
  :root {
    --stage: #969696;
    --card-white: #ffffff;
    --sky-top: #86d3f5;
    --sky-mid: #c4e9fa;
    --brand-blue: #1b449c;
    --brand-orange: #f47e2c;
    --ink-dark: #222222;
    --ink-grey: #6d6e71;
    --icon-top: #9a4a78;
    --icon-bottom: #26418f;
  }
  * { box-sizing: border-box; margin: 0; padding: 0; }
  html, body {
    width: 1200px; height: 1000px; overflow: hidden;
    background: var(--stage);
    font-family: "Montserrat", sans-serif;
  }
  .card {
    position: absolute;
    width: 779px; height: 448px;
    background: var(--card-white);
    overflow: hidden;
  }
  .card--front {
    left: 211px; top: 31px;
    border-radius: 0 100px 0 100px;
    background: linear-gradient(180deg, var(--sky-top) 0%, var(--sky-mid) 40%, #eef8fe 78%, var(--card-white) 100%);
  }
  .card--back {
    left: 207px; top: 509px;
    border-radius: 100px 0 100px 0;
  }
  .brand {
    position: absolute;
    display: flex; align-items: center;
  }
  .brand__dot {
    border-radius: 50%;
    background: var(--brand-orange);
    flex: none;
  }
  .brand__name {
    color: var(--brand-blue);
    font-weight: 800;
    text-transform: uppercase;
    line-height: 1;
  }
  .card--front .brand {
    left: 0; right: 0; top: 205px; justify-content: center; gap: 22px;
  }
  .card--front .brand__dot { width: 56px; height: 56px; }
  .card--front .brand__name { font-size: 44px; letter-spacing: 1px; }
  .services {
    position: absolute; left: 0; right: 0; top: 384px;
    text-align: center;
    color: var(--ink-grey);
    font-size: 20.5px; font-weight: 600;
  }
  .card--back .brand {
    right: 50px; top: 572px; top: 62px; gap: 10px;
  }
  .card--back .brand__dot { width: 26px; height: 26px; }
  .card--back .brand__name { font-size: 20px; letter-spacing: 0.5px; }
  .contact {
    position: absolute; left: 0; right: 0; top: 178px;
    text-align: center;
  }
  .contact__name {
    font-size: 27px; font-weight: 800; letter-spacing: 2.4px;
    text-transform: uppercase; line-height: 1.2;
  }
  .contact__first { color: var(--brand-blue); }
  .contact__last { color: var(--brand-orange); }
  .contact__role {
    font-size: 26px; font-weight: 500; letter-spacing: 2px;
    color: var(--ink-dark); line-height: 1.2; margin-top: 2px;
  }
  .contact__icons {
    display: flex; justify-content: center; gap: 6px; margin-top: 9px;
  }
  .contact__icons svg { width: 28px; height: 28px; display: block; }
  .contact__line {
    font-size: 19.5px; color: var(--ink-grey); line-height: 26px;
  }
  .contact__phone { margin-top: 16px; }
  .contact__license { margin-top: 23px; }
</style>
</head>
<body>
  <section class="card card--front" aria-label="Business card front">
    <div class="brand">
      <span class="brand__dot"></span>
      <span class="brand__name">Breezeway Comfort</span>
    </div>
    <p class="services">SALES • SERVICE • INSTALLATION • MAINTENANCE</p>
  </section>

  <section class="card card--back" aria-label="Business card back">
    <div class="brand">
      <span class="brand__dot"></span>
      <span class="brand__name">Breezeway Comfort</span>
    </div>
    <div class="contact">
      <p class="contact__name"><span class="contact__first">Marcus</span> <span class="contact__last">Tollefsen</span></p>
      <p class="contact__role">Owner</p>
      <div class="contact__icons">
        <svg viewBox="0 0 28 28" aria-label="Phone">
          <defs>
            <linearGradient id="icon-fill" x1="0" y1="0" x2="0" y2="1">
              <stop offset="0" stop-color="var(--icon-top)"/>
              <stop offset="1" stop-color="var(--icon-bottom)"/>
            </linearGradient>
          </defs>
          <circle cx="14" cy="14" r="14" fill="url(#icon-fill)"/>
          <path d="M10.2 7.5c.6-.4 1.3-.2 1.6.4l1 2.1c.3.5.1 1.1-.3 1.5l-.8.6c.6 1.5 1.7 2.8 3.1 3.6l.7-.7c.4-.4 1-.5 1.5-.2l2 1.1c.6.3.8 1.1.4 1.6l-.9 1.2c-.5.6-1.3.8-2 .6-3.4-1.1-6-3.9-6.9-7.4-.2-.7 0-1.5.6-2z" fill="#fff"/>
        </svg>
        <svg viewBox="0 0 28 28" aria-label="Email">
          <circle cx="14" cy="14" r="14" fill="url(#icon-fill)"/>
          <rect x="7.5" y="9.5" width="13" height="9" rx="1" fill="none" stroke="#fff" stroke-width="1.4"/>
          <path d="M7.8 10l6.2 4.8 6.2-4.8M7.8 18l4.6-4M20.2 18l-4.6-4" fill="none" stroke="#fff" stroke-width="1.2"/>
        </svg>
      </div>
      <p class="contact__line contact__phone">555-382-4071</p>
      <p class="contact__line">breezewaycomfortair@mailvista.example</p>
      <p class="contact__line contact__license">License # 2874590</p>
    </div>
  </section>
</body>
</html>
```